AI Business Tools Landing Page

My web-based website builder (Nurvanta.com) will be adding many new features in the very near future and I need an eye-catching landing page to promote these new products.

The page will have a primary section of the 8 main products we are promoting:
1. AI Instant Website Generator
2. AI Chatbot
3. Online Store Builder with AI Assistance
4. AI Auto-Blogging System
5. Online Scheduling System
6. Custom Email System
7. SEO Service
8. CRM System

The page will also have a smaller section for links to our affiliate programs. These can be smaller, less-promanent buttons or links. These are the affiliate products:
1. Get Your LLC
2. Website Design and Maintenance
3. Tavolin Ads Management
4. Social Media Posting Service
5. Logo Design
6. Trademark Registration
7. Patent Application
8. Printing Services (including postcards, flyers, and merch.)
9. Bulk AI Content Generator

The theme and color scheme of the page should follow the theme of our main website, which is https://nurvanta.com.

I need the page fully coded and ready to deploy on my server.

I look forward to seeing your amazing designs!

```html
<!DOCTYPE html>
<html lang="en">
<head>
<meta charset="utf-8">
<title>Nurvanta – AI Business Tools</title>
<link href="https://fonts.googleapis.com/css2?family=Poppins:ital,wght@0,400;0,500;0,600;0,700;1,400&display=swap" rel="stylesheet">
<style>
:root{
  --navy:#04182b;
  --navy-2:#072440;
  --navy-3:#0a2d4f;
  --line:#1f74c9;
  --cyan:#38c6ea;
  --blue:#1c74e6;
  --blue-dark:#0b2440;
  --white:#ffffff;
  --muted:#b9c7d6;
  --ink:#0d1f33;
  --ink-soft:#3c4a5a;
}
*{box-sizing:border-box;margin:0;padding:0}
html,body{width:1200px;height:4525px;overflow:hidden}
body{font-family:'Poppins',sans-serif;background:var(--navy);color:var(--white);position:relative}
a{color:inherit;text-decoration:none}
.abs{position:absolute}

/* header & hero */
.hero{position:absolute;left:0;top:0;width:1200px;height:643px;background:linear-gradient(115deg,#1a63dd 0%,#2590ea 50%,#3fd0f0 100%);overflow:hidden}
.brand{display:flex;align-items:center;gap:10px;font-weight:600;color:var(--white)}
.brand-dot{width:30px;height:30px;border-radius:50%;background:var(--white)}
.hero .brand{position:absolute;left:112px;top:26px;font-size:26px}
.nav{position:absolute;left:327px;top:36px;display:flex;gap:22px;font-size:10px}
.btn{display:inline-flex;align-items:center;justify-content:center;border-radius:20px;font-size:10px;font-weight:500}
.btn-white{background:var(--white);color:var(--ink)}
.btn-navy{background:var(--blue-dark);color:var(--white)}
.btn-outline{border:1.5px solid var(--white);color:var(--white)}
.nav-cta{position:absolute;left:852px;top:37px;width:137px;height:31px}
.nav-login{position:absolute;left:1003px;top:37px;width:85px;height:31px}
.hero h1{position:absolute;left:109px;top:186px;font-size:51px;line-height:60px;font-weight:600;width:560px}
.hero-sub{position:absolute;left:109px;top:385px;font-size:12px;line-height:19px;width:360px}
.hero-btn1{position:absolute;left:109px;top:446px;width:116px;height:30px}
.hero-btn2{position:absolute;left:235px;top:446px;width:116px;height:30px}
.hero-art{position:absolute;left:590px;top:130px;width:610px;height:513px;background:radial-gradient(ellipse at 40% 35%,rgba(255,120,40,.75) 0%,rgba(200,220,240,.55) 30%,rgba(60,180,235,0) 70%)}

/* section headings */
.eyebrow{font-size:15px;letter-spacing:2px;color:var(--cyan);font-weight:500}
.center{left:0;width:1200px;text-align:center}
.sec-title{font-size:40px;font-weight:600;line-height:48px}
.sec-desc{font-size:12px;line-height:20px;color:var(--white)}

/* product cards */
.glow{position:absolute;border-radius:50%;background:radial-gradient(circle,rgba(30,140,200,.35) 0%,rgba(4,24,43,0) 70%)}
.card{position:absolute;border:1.5px solid var(--line);border-radius:6px;background:rgba(4,24,43,.6)}
.card .icon{position:absolute;right:14px;top:12px;width:46px;height:46px}
.card h3{position:absolute;left:20px;font-size:19px;font-weight:500;line-height:25px}
.card p{position:absolute;left:20px;right:18px;font-size:10px;line-height:17px;color:var(--white)}
.card .more{position:absolute;left:20px;font-size:9.5px;color:var(--cyan)}
.prod{width:234px;height:223px}
.prod h3{top:72px}
.prod p{top:124px}
.prod .more{top:185px}

/* about */
.about{position:absolute;left:112px;top:1462px;width:976px;height:302px;background:var(--white);border-radius:30px;color:var(--ink)}
.about .eyebrow{position:absolute;left:53px;top:58px}
.about h2{position:absolute;left:53px;top:86px;font-size:40px;line-height:50px;font-weight:600;color:var(--blue-dark)}
.about p{position:absolute;left:452px;width:450px;font-size:10.5px;line-height:19px;color:var(--ink-soft)}
.about .btn{position:absolute;left:452px;top:225px;width:118px;height:30px}

/* affiliates */
.aff{width:315px;height:265px}
.aff .icon{width:56px;height:56px}
.aff h3{top:88px}
.aff p{top:140px;left:26px;right:24px}
.aff h3,.aff .more{left:26px}
.aff .more{top:230px}
.arrow{position:absolute;width:42px;height:42px;border-radius:50%;background:var(--blue)}

/* why us */
.why-title{position:absolute;left:112px;top:2377px;font-size:40px;line-height:46px;font-weight:600}
.why-intro{position:absolute;left:112px;top:2467px;width:390px;font-size:12px;line-height:19px}
.feat h4{position:absolute;left:170px;font-size:19px;font-weight:500}
.feat p{position:absolute;left:170px;width:330px;font-size:10.5px;line-height:18px}
.feat svg{position:absolute;left:112px;width:42px;height:42px}
.why-photo{position:absolute;left:610px;top:2349px;width:590px;height:626px;background:linear-gradient(110deg,#1c3a55 0%,#4d6c86 45%,#a9b9c8 75%,#2d4b66 100%)}

/* testimonials */
.tcard{position:absolute;width:475px;height:309px;border:1.5px solid var(--line);border-radius:6px;background:var(--navy)}
.avatar{position:absolute;left:26px;top:30px;width:62px;height:62px;border-radius:50%;background:linear-gradient(135deg,#8a6a52,#2c3844)}
.tname{position:absolute;left:112px;top:36px;font-size:19px;font-weight:500}
.trole{position:absolute;left:112px;top:68px;font-size:10.5px}
.tquote{position:absolute;left:26px;right:26px;top:124px;font-size:10.5px;line-height:19px;font-style:italic;color:var(--muted)}

/* cta */
.cta{position:absolute;left:112px;top:3672px;width:976px;height:439px;border-radius:36px;background:linear-gradient(110deg,#1a68de 0%,#2c9ee9 60%,#40ccef 100%);overflow:hidden}
.cta .eyebrow{position:absolute;left:44px;top:66px;color:var(--white)}
.cta h2{position:absolute;left:44px;top:112px;font-size:40px;line-height:48px;font-weight:600}
.cta p{position:absolute;left:44px;top:219px;width:540px;font-size:12px;line-height:20px}
.cta .btn{position:absolute;left:48px;top:343px;width:114px;height:28px}
.cta-art{position:absolute;left:588px;top:100px;width:388px;height:339px;background:radial-gradient(ellipse at 55% 50%,rgba(230,240,250,.85) 0%,rgba(120,200,240,.4) 45%,rgba(64,204,239,0) 75%)}

/* footer */
.footer{position:absolute;left:0;top:4111px;width:1200px;height:414px;background:linear-gradient(180deg,#04182b 0%,#05203a 100%)}
.footer .brand{position:absolute;left:112px;top:120px;font-size:34px}
.footer .brand-dot{width:40px;height:40px}
.f-about{position:absolute;left:112px;top:192px;width:250px;font-size:10.5px;line-height:18px}
.f-col{position:absolute;top:122px}
.f-col h5{font-size:14px;font-weight:500;margin-bottom:14px}
.f-col li{list-style:none;font-size:10.5px;line-height:22.5px}
.f-input{position:absolute;left:889px;top:154px;width:197px;height:30px;border:1px solid var(--white);border-radius:16px;font-size:9px;padding:8px 16px}
.f-sub{position:absolute;left:889px;top:199px;width:197px;height:30px}
.f-rule{position:absolute;left:50px;top:334px;width:1100px;height:1px;background:rgba(255,255,255,.5)}
.f-copy{position:absolute;left:0;top:370px;width:1200px;text-align:center;font-size:14px}
</style>
</head>
<body>

<section class="hero">
  <a class="brand" href="https://nurvanta.com"><span class="brand-dot"></span>Nurvanta</a>
  <nav class="nav"><a>Products</a><a>About Us</a><a>Make Money</a><a>History of AI</a><a>Pricing</a><a>Blog</a><a>Contact Us</a></nav>
  <a class="btn btn-white nav-cta">Get Started for FREE!</a>
  <a class="btn btn-outline nav-login">Login</a>
  <h1>Unlock the Future of Website Building with AI Tools</h1>
  <p class="hero-sub">Create, manage, and grow your online presence with AI-powered tools designed for success</p>
  <a class="btn btn-white hero-btn1">Get In Touch</a>
  <a class="btn btn-navy hero-btn2">Learn More</a>
  <div class="hero-art" role="img" aria-label="Robotic hand holding a glowing AI head"></div>
</section>

<div class="glow" style="left:700px;top:1100px;width:700px;height:700px"></div>
<div class="glow" style="left:-250px;top:1350px;width:600px;height:600px"></div>

<p class="abs center eyebrow" style="top:703px">Our Products</p>
<h2 class="abs center sec-title" style="top:735px">Discover Our AI Business Tools</h2>
<p class="abs center sec-desc" style="top:798px">Lorem Ipsum has been the industry's standard dummy text ever since the 1500s, when an<br>unknown printer took a galley of type and scrambled it to make a type specimen book.</p>

<svg width="0" height="0" style="position:absolute">
  <symbol id="ico" viewBox="0 0 46 46"><rect x="8" y="6" width="30" height="26" rx="3" fill="none" stroke="#38c6ea" stroke-width="1.6"/><path d="M14 14h18M14 20h12M23 32v6M15 40h16" stroke="#38c6ea" stroke-width="1.6" fill="none"/></symbol>
</svg>

<article class="card prod" style="left:112px;top:870px"><svg class="icon"><use href="#ico"/></svg><h3>AI Instant Website Generator</h3><p>Get a professional, SEO-optimized website in seconds!...</p><a class="more">Read More &nbsp;››</a></article>
<article class="card prod" style="left:360px;top:870px"><svg class="icon"><use href="#ico"/></svg><h3>ChatBot</h3><p style="top:98px">Fully-trainable ChatBot will learn about your business to automate</p><a class="more" style="top:159px">Read More &nbsp;››</a></article>
<article class="card prod" style="left:606px;top:870px"><svg class="icon"><use href="#ico"/></svg><h3>Online Store Builder with AI Assistance</h3><p>Sell you products online and integrate your products into any...</p><a class="more">Read More &nbsp;››</a></article>
<article class="card prod" style="left:854px;top:870px"><svg class="icon"><use href="#ico"/></svg><h3>AI Auto-Blogging System</h3><p>AI will generate an incredible blog for your business in seconds...</p><a class="more">Read More &nbsp;››</a></article>

<article class="card prod" style="left:112px;top:1112px"><svg class="icon"><use href="#ico"/></svg><h3>Online Scheduling System</h3><p>Get a professional, SEO-optimized website in seconds!...</p><a class="more">Read More &nbsp;››</a></article>
<article class="card prod" style="left:360px;top:1112px"><svg class="icon"><use href="#ico"/></svg><h3>Custom emails using your domain</h3><p>Fully-trainable ChatBot will learn about your business to automate</p><a class="more">Read More &nbsp;››</a></article>
<article class="card prod" style="left:606px;top:1112px"><svg class="icon"><use href="#ico"/></svg><h3>SEO Service – Automatic Backlink Building.</h3><a class="more">Read More &nbsp;››</a></article>
<article class="card prod" style="left:854px;top:1112px"><svg class="icon"><use href="#ico"/></svg><h3>CRM System</h3><p style="top:98px">AI will generate an incredible blog for your business in seconds...</p><a class="more" style="top:159px">Read More &nbsp;››</a></article>

<a class="btn btn-white abs" style="left:476px;top:1374px;width:116px;height:30px">Contact Us</a>
<a class="btn btn-outline abs" style="left:607px;top:1374px;width:116px;height:30px">Get Product</a>

<section class="about">
  <p class="eyebrow">About Nurvanta</p>
  <h2>Discover the Best<br>AI Website Builder</h2>
  <p style="top:54px">In the journey of turning dreams into digital realities, we recognize the evolving nature of your digital needs. This understanding is at the heart of our premium plans, meticulously crafted to support your growing ambitions.</p>
  <p style="top:130px">Our premium offerings unlock the potential of multi-page designs, enhanced e-commerce capabilities, and exclusive access to a premium image gallery, ensuring your website not only meets but exceeds expectations.</p>
  <a class="btn btn-navy">Learn More</a>
</section>

<p class="abs center eyebrow" style="top:1830px">What We Serve</p>
<h2 class="abs center sec-title" style="top:1861px">Explore Our Affiliate Services</h2>
<p class="abs center sec-desc" style="top:1924px">Lorem Ipsum has been the industry's standard dummy text ever since the 1500s, when an<br>unknown printer took a galley of type and scrambled it to make a type specimen book.</p>

<a class="arrow" style="left:48px;top:2109px" aria-label="Previous"><svg width="42" height="42"><path d="M27 21H15m5-5-5 5 5 5" stroke="#fff" stroke-width="1.8" fill="none"/></svg></a>
<article class="card aff" style="left:112px;top:1998px"><svg class="icon"><use href="#ico"/></svg><h3>Website Design and Maintenance</h3><p>Lorem Ipsum has been the industry's standard dummy text ever since the 1500s, when an unknown printer took a galley of type and scrambled it to make a type specimen book.</p><a class="more">Read More &nbsp;››</a></article>
<article class="card aff" style="left:443px;top:1998px"><svg class="icon"><use href="#ico"/></svg><h3>Tavolin Ads Management</h3><p>Lorem Ipsum has been the industry's standard dummy text ever since the 1500s, when an unknown printer took a galley of type and scrambled it to make a type specimen book.</p><a class="more">Read More &nbsp;››</a></article>
<article class="card aff" style="left:771px;top:1998px"><svg class="icon"><use href="#ico"/></svg><h3>Social Media Posting Service</h3><p>Lorem Ipsum has been the industry's standard dummy text ever since the 1500s, when an unknown printer took a galley of type and scrambled it to make a type specimen book.</p><a class="more">Read More &nbsp;››</a></article>
<a class="arrow" style="left:1106px;top:2109px" aria-label="Next"><svg width="42" height="42"><path d="M15 21h12m-5-5 5 5-5 5" stroke="#fff" stroke-width="1.8" fill="none"/></svg></a>

<p class="abs eyebrow" style="left:112px;top:2329px">Why Choose Us</p>
<h2 class="why-title">The Top Reasons to<br>Partner with Us</h2>
<p class="why-intro">Nurvanta leverages AI technology to streamline the website creation process, making it faster, more efficient, and incredibly user-friendly. Here's what sets Nurvanta apart:</p>
<div class="feat">
  <svg style="top:2546px"><use href="#ico"/></svg>
  <h4 style="top:2548px">Mobile Optimization</h4>
  <p style="top:2584px">Nurvanta ensures your website is beautifully rendered on PCs, smartphones, and tablets, offering a seamless user experience across all devices.</p>
  <svg style="top:2655px"><use href="#ico"/></svg>
  <h4 style="top:2657px">Unparalleled Flexibility</h4>
  <p style="top:2697px">Customize your site with ease, adding custom images, content, and more to truly make it your own.</p>
  <svg style="top:2758px"><use href="#ico"/></svg>
  <h4 style="top:2760px">Zero Cost to Start</h4>
  <p style="top:2795px">Dive into the world of website creation without any initial investment. Nurvanta offers a free platform to build your website, providing a cost-effective solution for businesses and individuals alike.</p>
  <svg style="top:2885px"><use href="#ico"/></svg>
  <h4 style="top:2887px">Robust Cloud Infrastructure</h4>
  <p style="top:2924px">Benefit from a secure, high-powered cloud computing environment that guarantees reliability and speed for all Nurvanta websites.</p>
</div>
<div class="why-photo" role="img" aria-label="Man using a tablet beside a humanoid robot"></div>

<p class="abs center eyebrow" style="top:3038px">Testimonial</p>
<h2 class="abs center sec-title" style="top:3072px">What Our Clients Say</h2>
<p class="abs center sec-desc" style="top:3134px">Lorem Ipsum has been the industry's standard dummy text ever since the 1500s, when an<br>unknown printer took a galley of type and scrambled it to make a type specimen book.</p>

<a class="arrow" style="left:48px;top:3424px" aria-label="Previous"><svg width="42" height="42"><path d="M27 21H15m5-5-5 5 5 5" stroke="#fff" stroke-width="1.8" fill="none"/></svg></a>
<article class="tcard" style="left:112px;top:3205px">
  <div class="avatar" role="img" aria-label="Client portrait"></div>
  <p class="tname">Dario L.</p><p class="trole">Freelance Photographer</p>
  <p class="tquote">Nurvanta is a game-changer! My photography portfolio looks absolutely stunning. The intuitive design tools and instant results have saved me both time and money. Highly recommend!Nurvanta is a game-changer! My photography portfolio looks absolutely stunning. The intuitive design tools and instant results have saved me both time and money. Highly recommend!Nurvanta is a game-changer! My photography portfolio looks absolutely stunning. The intuitive design tools and instant results have saved me both time and money. Highly recommend!</p>
</article>
<article class="tcard" style="left:611px;top:3293px">
  <div class="avatar" role="img" aria-label="Client portrait"></div>
  <p class="tname">Dario L.</p><p class="trole">Freelance Photographer</p>
  <p class="tquote">Nurvanta is a game-changer! My photography portfolio looks absolutely stunning. The intuitive design tools and instant results have saved me both time and money. Highly recommend!Nurvanta is a game-changer! My photography portfolio looks absolutely stunning. The intuitive design tools and instant results have saved me both time and money. Highly recommend!Nurvanta is a game-changer! My photography portfolio looks absolutely stunning. The intuitive design tools and instant results have saved me both time and money. Highly recommend!</p>
</article>
<a class="arrow" style="left:1106px;top:3424px" aria-label="Next"><svg width="42" height="42"><path d="M15 21h12m-5-5 5 5-5 5" stroke="#fff" stroke-width="1.8" fill="none"/></svg></a>

<section class="cta">
  <p class="eyebrow">Get In Touch</p>
  <h2>Stop waiting. Start<br>building. Try for free now!</h2>
  <p>Harness the power of AI and embark on your website creation journey with Nurvanta. Whether you're looking to launch a new business, showcase your portfolio, or start a blog, Nurvanta is your go-to AI Website Builder, ready to bring your digital vision to life. Explore the limitless possibilities of AI-driven website creation and let Nurvanta transform your online presence today.</p>
  <a class="btn btn-white">Contact Us</a>
  <div class="cta-art" role="img" aria-label="Robotic hand touching a glowing AI panel"></div>
</section>

<footer class="footer">
  <a class="brand" href="https://nurvanta.com"><span class="brand-dot"></span>Nurvanta</a>
  <p class="f-about">In the rapidly evolving digital era, the integration of Artificial Intelligence (AI) into various sectors is unmistakably transformative.</p>
  <div class="f-col" style="left:467px"><h5>Company Links</h5><ul><li>Products</li><li>About Us</li><li>Make Money</li><li>History of AI</li><li>Pricing</li><li>Blog</li><li>Contact Us</li></ul></div>
  <div class="f-col" style="left:676px"><h5>Contact Info</h5><ul><li>Terms &amp; Conditions</li><li>FAQ</li><li>Privacy Policy</li><li>Contact Us</li></ul></div>
  <div class="f-col" style="left:889px"><h5>Subscribe Newsletter</h5></div>
  <div class="f-input">Email</div>
  <a class="btn btn-white f-sub">Subscribe</a>
  <div class="f-rule"></div>
  <p class="f-copy">© 2024 Nurvanta. All Rights Reserved</p>
</footer>

</body>
</html>
```